Harlow Ridge Partners Business Cards

Design Business cards in a format where I can change the information and utilize a third party buisness card printing company

Contact Information for Business Card

Want Logo and Name on Back. Looking for Spot UV style shine on Logo. Probably Black background. Want smaller logo on front with contact details. Like rounded edges or something else interesting.

Requirements
Must have
• Strong masculine look.

```html
<!DOCTYPE html>
<html lang="en">
<head>
<meta charset="utf-8">
<title>Harlow Ridge Partners – Business Cards</title>
<link href="https://fonts.googleapis.com/css2?family=Cinzel:wght@500&family=Marcellus&display=swap" rel="stylesheet">
<style>
  :root {
    --backdrop: #3b3b3d;
    --card: #1e1f21;
    --card-edge: #2a2b2e;
    --mark-area: #2c2d30;
    --ink: #f4f4f4;
    --ink-soft: #d8d8d8;
    --band: #8a8a8c;
    --band-ink: #1e1f21;
  }
  * { box-sizing: border-box; margin: 0; padding: 0; }
  html, body {
    width: 799px; height: 1200px; overflow: hidden;
    background: var(--backdrop);
  }
  .sheet { position: relative; width: 799px; height: 1200px; }
  .card {
    position: absolute; left: 70px; width: 660px; height: 377px;
    background: var(--card);
    border-radius: 24px;
    border: 1px solid var(--card-edge);
    overflow: hidden;
    color: var(--ink);
  }
  .card--front { top: 110px; }
  .card--back { top: 710px; }

  .wordmark { font-family: "Cinzel", serif; font-weight: 500; color: var(--ink); line-height: 1; }
  .wordmark__main { font-size: 38px; letter-spacing: 1px; display: block; white-space: nowrap; }
  .wordmark__sub { font-size: 13px; letter-spacing: 14px; display: block; margin-top: 4px; text-align: center; }

  .spot-uv-mark {
    position: absolute; left: 44px; top: 40px;
    width: 250px; height: 250px;
    background: var(--mark-area);
  }
  .card--front .website {
    position: absolute; top: 52px; right: 44px;
    font-family: "Marcellus", serif; font-size: 17px; color: var(--ink-soft);
  }
  .card--front .wordmark {
    position: absolute; right: 44px; bottom: 58px; text-align: right;
  }

  .card--back .brand {
    position: absolute; left: 40px; top: 66px; width: 300px;
    display: flex; flex-direction: column; align-items: center;
  }
  .brand__square { width: 46px; height: 46px; background: var(--ink); margin-bottom: 22px; }
  .card--back .wordmark__main { font-size: 34px; }

  .contact {
    position: absolute; left: 380px; top: 82px; width: 270px;
    font-family: "Marcellus", serif; color: var(--ink-soft);
  }
  .contact__name { font-family: "Cinzel", serif; font-size: 25px; color: var(--ink); letter-spacing: 1px; }
  .contact__role { font-size: 14px; margin-bottom: 14px; }
  .contact__address { font-size: 14px; line-height: 1.35; margin-bottom: 8px; }
  .contact__line { display: flex; align-items: center; gap: 8px; font-size: 14px; line-height: 1.5; white-space: nowrap; }
  .contact__line svg { width: 14px; height: 14px; fill: var(--ink); flex: none; }

  .band { position: absolute; left: 0; bottom: 0; width: 660px; height: 80px; }
  .band__url {
    position: absolute; left: 290px; bottom: 22px;
    font-family: "Marcellus", serif; font-size: 17px; color: var(--band-ink);
  }
</style>
</head>
<body>
<main class="sheet">

  <section class="card card--front" aria-label="Card front">
    <div class="spot-uv-mark" role="img" aria-label="Large gloss spot-UV brand mark area"></div>
    <p class="website">www.harlowridgepartners.com</p>
    <div class="wordmark">
      <span class="wordmark__main">Harlow Ridge</span>
      <span class="wordmark__sub">PARTNERS</span>
    </div>
  </section>

  <section class="card card--back" aria-label="Card back">
    <div class="brand">
      <span class="brand__square"></span>
      <div class="wordmark">
        <span class="wordmark__main">Harlow Ridge</span>
        <span class="wordmark__sub">PARTNERS</span>
      </div>
    </div>

    <div class="contact">
      <p class="contact__name">Declan Moore</p>
      <p class="contact__role">Managing Director</p>
      <p class="contact__address">88 Quarry Lane, Stonebridge,<br>Eastvale, US 40213</p>
      <p class="contact__line">
        <svg viewBox="0 0 16 16" aria-hidden="true"><path d="M3 1h3l1.5 4-2 1.2a9 9 0 0 0 4.3 4.3l1.2-2 4 1.5v3a2 2 0 0 1-2 2A13 13 0 0 1 1 3a2 2 0 0 1 2-2z"/></svg>
        (555) 014-2790
      </p>
      <p class="contact__line">
        <svg viewBox="0 0 16 16" aria-hidden="true"><path d="M1 3h14v10H1zM2.5 4.5v.4L8 9l5.5-4.1v-.4z" fill-rule="evenodd"/></svg>
        declan@harlowridgepartners.com
      </p>
    </div>

    <svg class="band" viewBox="0 0 660 80" preserveAspectRatio="none" aria-hidden="true">
      <path d="M0 80 V64 H230 Q250 64 256 44 L262 26 Q268 8 290 8 H660 V80 Z" fill="var(--band)"/>
    </svg>
    <p class="band__url">www.harlowridgepartners.com</p>
  </section>

</main>
</body>
</html>
```